Request for Business Card Design

Hi. My name is Marlena, I am looking for a new business card design for my company, Quillbrook Sensing Systems, LLC. I really like the design you did for Tavel Harvest and was hoping you could do something similar using our full logo and our mark. I am also open to any raised texture design using our mark. I have attached our full logo, which would need to be somewhere on the card, as well as the mark in both outline and full form, as well as our brand colors / guide. The card does not have to be white, as long as our logo and mark appear. I actually like darker colored business cards more, but am open to all options. If you are interested in working with me, please let me know. We would also take the business card design into letterhead design if you can do that.

```html
<!DOCTYPE html>
<html lang="en">
<head>
<meta charset="utf-8">
<title>Quillbrook Sensing Systems — Business Card</title>
<link href="https://fonts.googleapis.com/css2?family=Barlow:wght@400;500;700&display=swap" rel="stylesheet">
<style>
  :root {
    --backdrop: #7f97b8;
    --green: #7cc142;
    --green-light: #8ccc52;
    --blue: #2aa4cc;
    --charcoal: #3e3e41;
    --rule: #3a3b3d;
    --white: #ffffff;
    --mark-blue: #31a9d1;
  }
  * { box-sizing: border-box; margin: 0; padding: 0; }
  html, body {
    width: 1200px; height: 876px; overflow: hidden;
    background: var(--backdrop);
    font-family: "Barlow", "Helvetica Neue", Arial, sans-serif;
  }
  .canvas {
    width: 1200px; height: 876px;
    display: flex; align-items: center; justify-content: center; gap: 60px;
  }
  .card {
    position: relative;
    width: 520px; height: 297px;
    border-radius: 20px;
    overflow: hidden;
    box-shadow: 0 10px 24px rgba(30, 45, 70, 0.35);
  }

  /* Front */
  .card-front {
    background: linear-gradient(135deg, var(--green-light), var(--green));
    color: var(--white);
  }
  .brand {
    position: absolute; top: 42px; left: 0; right: 0;
    display: flex; align-items: center; justify-content: center; gap: 14px;
  }
  .brand-dot {
    width: 40px; height: 40px; border-radius: 50%;
    background: var(--white);
  }
  .brand-text { display: flex; flex-direction: column; }
  .brand-name {
    font-weight: 700; font-size: 34px; letter-spacing: 3px; line-height: 1;
  }
  .brand-tagline {
    font-weight: 500; font-size: 9.5px; letter-spacing: 0.6px; margin-top: 4px;
    text-transform: uppercase;
  }
  .name-band {
    position: absolute; left: 0; right: 0; top: 142px; height: 62px;
    background: var(--blue);
    border-top: 5px solid var(--rule);
    border-bottom: 5px solid var(--rule);
    display: flex; flex-direction: column; justify-content: center; align-items: center;
  }
  .person-name {
    font-weight: 500; font-size: 24px; letter-spacing: 1px; line-height: 1;
    text-transform: uppercase;
  }
  .person-role { font-size: 14px; margin-top: 3px; }
  .contacts {
    position: absolute; left: 18px; right: 18px; top: 226px;
    display: flex; justify-content: space-between;
  }
  .contact { display: flex; align-items: flex-start; gap: 8px; }
  .contact-icon { width: 24px; height: 24px; flex: none; }
  .contact-lines { font-size: 11.5px; line-height: 1.35; }

  /* Back */
  .card-back {
    background: linear-gradient(140deg, #4a4a4d, var(--charcoal) 60%, #333336);
    display: flex; align-items: center; justify-content: center; gap: 18px;
  }
  .back-dot {
    width: 54px; height: 54px; border-radius: 50%;
    background: var(--mark-blue);
  }
  .back-name {
    color: var(--mark-blue);
    font-weight: 700; font-size: 44px; letter-spacing: 4px;
  }
</style>
</head>
<body>
<main class="canvas">

  <section class="card card-front" aria-label="Business card front">
    <div class="brand">
      <span class="brand-dot"></span>
      <div class="brand-text">
        <span class="brand-name">QUILLBROOK</span>
        <span class="brand-tagline">Sensing Systems</span>
      </div>
    </div>

    <div class="name-band">
      <span class="person-name">Marlena Voss</span>
      <span class="person-role">Director</span>
    </div>

    <div class="contacts">
      <div class="contact">
        <svg class="contact-icon" viewBox="0 0 24 24" aria-hidden="true">
          <circle cx="12" cy="12" r="12" fill="#fff"/>
          <rect x="8.5" y="5.5" width="7" height="13" rx="1.5" fill="none" stroke="#7cc142" stroke-width="1.6"/>
          <circle cx="12" cy="16" r="0.9" fill="#7cc142"/>
        </svg>
        <div class="contact-lines">+000 55501 2468<br>+000 55501 2468</div>
      </div>
      <div class="contact">
        <svg class="contact-icon" viewBox="0 0 24 24" aria-hidden="true">
          <circle cx="12" cy="12" r="12" fill="#fff"/>
          <rect x="6" y="8" width="12" height="8" rx="1" fill="none" stroke="#7cc142" stroke-width="1.6"/>
          <path d="M6.5 8.5 L12 12.5 L17.5 8.5" fill="none" stroke="#7cc142" stroke-width="1.4"/>
        </svg>
        <div class="contact-lines">hello@quillbrook.example<br>quillbrook.example</div>
      </div>
      <div class="contact">
        <svg class="contact-icon" viewBox="0 0 24 24" aria-hidden="true">
          <circle cx="12" cy="12" r="12" fill="#fff"/>
          <path d="M12 19 C9 15 7.5 12.5 7.5 10.5 A4.5 4.5 0 0 1 16.5 10.5 C16.5 12.5 15 15 12 19 Z" fill="#7cc142"/>
          <circle cx="12" cy="10.5" r="1.7" fill="#fff"/>
        </svg>
        <div class="contact-lines">18 Brookline Way<br>Harbourton, 4417</div>
      </div>
    </div>
  </section>

  <section class="card card-back" aria-label="Business card back">
    <span class="back-dot"></span>
    <span class="back-name">QUILLBROOK</span>
  </section>

</main>
</body>
</html>
```